Bright Harbor Health (03)

We're designing a website to sell Medicare Supplements. Attached is the script we want to say and general layout, but please use your best knowledge to make it better. This platform should be extremely user-friendly, but we want to make it look fun and approachable! Most Insurance/medicare websites are very boring, drab, simple but we want this one to be more personalized, fun and sexy (but again, still user-friendly since our target demographic is 65+).

This homepage should include a fun and inviting quiz, the script is in the attachment below. It should also include the blurbs about what medicare supplements plans are and why they should buy them. Feel free to play around with cool fonts and imagery, we want the site to be engaging!

Target Market(s)

seniors

Industry/Entity Type

Insurance

Number of Pages Required

1 page

Requirements
Must have
• Quiz, company name and tag line, script
Nice to have
• fun, engaging elements

```html
<!DOCTYPE html>
<html lang="en">
<head>
<meta charset="utf-8">
<title>Bright Harbor Health – Medicare Supplement Plans</title>
<link rel="stylesheet" href="https://fonts.googleapis.com/css2?family=Open+Sans:wght@400;600;700&family=Fira+Sans+Condensed:wght@500;600;700&family=Montserrat:wght@500;700&display=swap">
<style>
:root{
  --blue:#1c6ae8;
  --blue-deep:#1457cc;
  --blue-dark:#0f47b0;
  --green:#4aa61c;
  --green-tab:#43b02a;
  --ink:#1b1b1b;
  --text:#333;
  --muted:#8a8a8a;
  --line:#d9d9d9;
  --soft:#f0f0f0;
  --white:#fff;
}
*{box-sizing:border-box;margin:0;padding:0}
html,body{width:1200px;height:4290px;overflow:hidden}
body{position:relative;font-family:"Open Sans",sans-serif;color:var(--text);background:var(--white)}
.abs{position:absolute}
.heading{font-family:"Fira Sans Condensed",sans-serif;font-weight:700;color:var(--ink);text-align:center}
.rule{width:70px;height:2px;background:var(--blue);margin:0 auto}

/* header */
.site-header{left:0;top:0;width:1200px;height:106px;background:var(--blue);color:var(--white);font-size:13px}
.site-header .row{position:absolute;left:0;width:1200px;display:flex;align-items:center}
.topline{top:0;height:46px;border-bottom:1px solid rgba(255,255,255,.25)}
.info{position:absolute;display:flex;align-items:center;gap:10px}
.info svg{width:14px;height:14px}
.brand-box{position:absolute;left:491px;top:0;width:218px;height:106px;border-left:1px solid rgba(255,255,255,.3);border-right:1px solid rgba(255,255,255,.3);display:flex;flex-direction:column;align-items:center;justify-content:center;gap:10px}
.brand-box .mark{width:36px;height:36px;background:var(--white)}
.brand-box .name{font-weight:700;font-size:15px;letter-spacing:.3px}
.socials{position:absolute;right:42px;top:12px;display:flex;gap:14px}
.socials span{width:22px;height:22px;border-radius:50%;background:rgba(255,255,255,.25)}
.main-nav{position:absolute;right:32px;top:66px;display:flex;gap:16px;font-size:14px}

/* hero */
.hero{left:0;top:106px;width:1200px;height:734px;background:linear-gradient(90deg,#e9ebee 0%,#f6f6f7 40%,#eceef0 75%,#dfe1e3 100%)}
.hero-person{left:50px;top:40px;width:400px;height:694px;background:linear-gradient(180deg,#c9a58c 0%,#eef0f2 35%,#f7f7f8 100%);border-radius:180px 180px 0 0}
.hero-title{left:443px;top:353px;height:51px;padding:0 14px;background:var(--blue);color:var(--white);font-family:"Fira Sans Condensed",sans-serif;font-weight:600;font-size:34px;line-height:51px;letter-spacing:.3px}
.hero-title::after{content:"";position:absolute;right:-18px;top:0;width:6px;height:55px;background:var(--blue);transform:skewX(-12deg)}
.hero-tagline{left:443px;top:416px;width:640px;font-size:27px;line-height:26px;color:var(--ink)}
.hero-copy{left:443px;top:503px;width:590px;font-size:15px;line-height:15px;color:var(--ink)}
.hero-copy p{margin-bottom:12px}
.cta{left:453px;top:712px;width:339px;height:67px;border-radius:34px;background:var(--green);color:var(--white);font-family:"Fira Sans Condensed",sans-serif;font-weight:600;font-size:34px;line-height:67px;text-align:center}
.appt-tab{left:1157px;top:369px;width:43px;height:160px;background:var(--green-tab);border-radius:14px 0 0 14px;color:var(--white);font-size:13px;writing-mode:vertical-rl;transform:rotate(180deg);display:flex;align-items:center;justify-content:center}

/* covers */
.covers{left:0;top:840px;width:1200px;height:571px;background:var(--white)}
.covers .heading{position:absolute;left:0;top:84px;width:1200px;font-size:26px}
.covers .rule{position:absolute;left:565px;top:122px}
.covers .lead{position:absolute;left:0;top:142px;width:1200px;text-align:center;font-size:14px;line-height:21px;color:var(--muted)}
.card{position:absolute;top:290px;width:230px;height:198px;border:1px solid var(--line);background:var(--white);text-align:center}
.card .hex{position:absolute;left:71px;top:-40px;width:88px;height:80px;clip-path:polygon(25% 0,75% 0,100% 50%,75% 100%,25% 100%,0 50%);background:var(--line);display:flex;align-items:center;justify-content:center}
.card .hex::before{content:"";position:absolute;inset:1px;clip-path:inherit;background:var(--white)}
.card .hex svg{position:relative;width:30px;height:30px}
.card h3{margin-top:60px;font-size:15px;font-weight:600;color:var(--ink);letter-spacing:.2px}
.card p{margin:14px 12px 0;font-size:13.5px;line-height:21px;color:var(--muted)}
.card .go{position:absolute;left:83px;bottom:-12px;width:64px;height:24px;border:1px solid var(--line);border-radius:12px;background:var(--white);display:flex;align-items:center;justify-content:center}

/* quiz */
.quiz{left:0;top:1411px;width:1200px;height:702px;background:var(--soft)}
.quiz-person{left:158px;top:37px;width:374px;height:665px;background:linear-gradient(180deg,#b58c6b 0%,#e8ebee 30%,#f8f8f9 60%,#d6dbe2 100%);border-radius:170px 170px 0 0}
.quiz .heading{position:absolute;left:521px;top:46px;font-size:26px;text-align:left}
.q{position:absolute;left:587px;font-size:24px;color:var(--ink)}
.opts{position:absolute;left:815px;font-size:25px;line-height:32px;color:var(--ink);list-style:none}
.opts li{display:flex;align-items:center;gap:9px}
.radio{width:16px;height:16px;border:2px solid var(--blue);border-radius:50%;display:inline-block;position:relative}
.radio.on::after{content:"";position:absolute;left:3px;top:3px;width:6px;height:6px;border-radius:50%;background:var(--blue)}
.zip{position:absolute;left:587px;top:506px;width:318px;height:43px;border:1px solid var(--line);background:var(--white);font-size:21px;font-style:italic;color:#b0b0b0;padding-left:12px;line-height:41px}
.submit{position:absolute;left:587px;top:577px;width:167px;height:59px;border-radius:30px;background:var(--blue);color:var(--white);font-family:"Fira Sans Condensed",sans-serif;font-weight:700;font-size:26px;line-height:59px;text-align:center}

/* explainer */
.explain{left:0;top:2113px;width:1200px;height:475px;background:var(--white)}
.explain .heading{position:absolute;left:0;top:66px;width:1200px;font-size:26px}
.explain .photo{left:72px;top:140px;width:316px;height:243px;background:linear-gradient(135deg,#7ea3c9 0%,#d9e2ec 50%,#f2e6dc 100%)}
.explain .body{position:absolute;left:429px;top:141px;width:690px;font-size:20.5px;line-height:21.5px;color:var(--ink)}
.explain .body p{margin-bottom:12px}
.explain .body ul{list-style:none}
.explain .body li::before{content:"";display:inline-block;width:15px;height:15px;border-radius:50%;background:var(--ink);margin-right:7px;vertical-align:-1px}

/* costs */
.costs{left:0;top:2588px;width:1200px;height:569px;background:var(--soft)}
.costs .heading{position:absolute;left:0;top:61px;width:1200px;font-size:26px}
.costs .rule{position:absolute;left:565px;top:100px}
.costs .body{position:absolute;left:62px;top:125px;width:698px;text-align:right;font-size:20.5px;line-height:21.5px;color:var(--ink)}
.costs .body p{margin-bottom:13px}
.costs .body p.item::before{content:"";display:inline-block;width:15px;height:15px;border-radius:50%;background:var(--ink);margin-right:6px;vertical-align:-1px}
.costs .photo{left:800px;top:126px;width:317px;height:241px;background:linear-gradient(135deg,#c9d9ea 0%,#f3f5f8 45%,#7fa4cc 100%)}

/* newsletter */
.newsletter{left:0;top:3157px;width:1200px;height:246px;background:var(--white)}
.newsletter h2{position:absolute;left:100px;top:76px;font-family:"Montserrat",sans-serif;font-weight:700;font-size:34px;line-height:40px;color:#1e2a3a}
.newsletter .divider{position:absolute;left:501px;top:78px;width:1px;height:80px;background:var(--line)}
.newsletter .label{position:absolute;left:634px;top:75px;font-family:"Montserrat",sans-serif;font-weight:500;font-size:19px;color:#1e2a3a}
.signup{position:absolute;left:634px;top:113px;width:469px;height:51px;border:1px solid #e6e6e6;border-radius:26px;background:var(--white);font-size:13px;color:var(--muted);line-height:49px;padding-left:18px;box-shadow:0 3px 8px rgba(0,0,0,.06)}
.signup .send{position:absolute;right:-1px;top:-1px;width:70px;height:51px;border-radius:0 26px 26px 0;background:var(--green-tab);display:flex;align-items:center;justify-content:center}

/* map */
.map{left:0;top:3403px;width:1200px;height:483px;background:linear-gradient(135deg,#4a4a3e 0%,#5c5a48 40%,#6b5f3f 60%,#47463e 100%)}
.map .zoom{position:absolute;left:10px;top:10px;width:30px;height:60px;background:var(--white);border-radius:2px;font-size:22px;color:#555;text-align:center;line-height:30px}
.map .full{position:absolute;right:10px;top:10px;width:30px;height:30px;background:var(--white);border-radius:2px}

/* footer */
.site-footer{left:0;top:3886px;width:1200px;height:349px;background:var(--blue);color:var(--white)}
.foot-brand{position:absolute;left:98px;top:87px;display:flex;align-items:center;gap:10px;font-weight:700;font-size:18px}
.foot-brand span.mark{width:36px;height:36px;background:var(--white)}
.foot-about{position:absolute;left:98px;top:144px;width:316px;font-size:13px;line-height:21px}
.foot-col{position:absolute;top:88px}
.foot-col h4{font-weight:400;font-size:21px;margin-bottom:18px}
.foot-col ul{list-style:none;font-size:13.5px;line-height:30px}
.foot-col li{display:flex;align-items:center;gap:12px}
.foot-col .dot{width:9px;height:9px;border-radius:50%;background:var(--white)}
.foot-col.find li{align-items:flex-start;line-height:21px;margin-bottom:9px}
.foot-col.find svg{width:14px;height:14px;margin-top:3px;flex:none}
.copyright{left:0;top:4235px;width:1200px;height:55px;background:var(--blue-dark);color:var(--white);font-size:12px;text-align:center;line-height:55px}
</style>
</head>
<body>

<header class="site-header abs">
  <div class="row topline">
    <div class="info" style="left:40px;top:15px">
      <svg viewBox="0 0 14 14"><rect x="1" y="2" width="12" height="11" rx="1" fill="none" stroke="#fff" stroke-width="1.5"/><line x1="1" y1="5.5" x2="13" y2="5.5" stroke="#fff" stroke-width="1.5"/></svg>
      <span>Monday - Friday 08:00-19:00</span>
    </div>
    <div class="info" style="left:315px;top:15px">
      <svg viewBox="0 0 14 14"><path d="M7 1a4.5 4.5 0 0 0-4.5 4.5C2.5 9 7 13 7 13s4.5-4 4.5-7.5A4.5 4.5 0 0 0 7 1z" fill="#fff"/><circle cx="7" cy="5.5" r="1.6" fill="#1c6ae8"/></svg>
      <span>PO. 4120, NY</span>
    </div>
  </div>
  <div class="info" style="left:40px;top:67px">
    <svg viewBox="0 0 14 14"><path d="M3 1l2.5 3-1.5 1.5a8 8 0 0 0 4.5 4.5L10 8.5l3 2.5-1.5 2C6 13 1 8 1 2.5z" fill="#fff"/></svg>
    <span>Call (800) 555-0148 to talk to a live agent.</span>
  </div>
  <div class="brand-box">
    <span class="mark"></span>
    <span class="name">BRIGHT HARBOR HEALTH</span>
  </div>
  <div class="socials"><span></span><span></span><span></span><span></span></div>
  <nav class="main-nav"><span>Home</span><span>About Us</span><span>New Policies</span><span>Contact Us</span></nav>
</header>

<section class="hero abs">
  <div class="hero-person abs" role="img" aria-label="Smiling female doctor in a white coat with a stethoscope, in a bright clinic hallway"></div>
  <div class="hero-title abs" style="left:443px;top:247px">BRIGHT HARBOR HEALTH</div>
  <p class="hero-tagline abs" style="top:310px">Be confident in choosing the Medicare Supplement plan that’s right for you.</p>
  <div class="hero-copy abs" style="top:398px">
    <p>We know insurance can be confusing. With so much information and not enough answers, we’re here to help you find the plan that works best for you, your family and your health.</p>
    <p>Take this short quiz to to find flexible and affordable plans that you can feel confident in.</p>
  </div>
  <div class="cta abs" style="top:606px">Take the Quiz Below</div>
  <div class="appt-tab abs" style="top:263px">Make Appointment</div>
</section>

<section class="covers abs">
  <h2 class="heading">OUR INSURANCE COVERS EVERYTHING</h2>
  <div class="rule"></div>
  <p class="lead">Lorem ipsum dolor sit amet, consectetur adipisicing elit sed<br>do eiusmod tempor incididunt ut labore.</p>

  <div class="card" style="left:100px">
    <div class="hex"><svg viewBox="0 0 30 30"><rect x="3" y="9" width="17" height="13" rx="2" fill="#8b5cf6"/><path d="M20 12h4l3 4v6h-7z" fill="#8b5cf6"/><circle cx="9" cy="23" r="2.5" fill="#8b5cf6"/><circle cx="22" cy="23" r="2.5" fill="#8b5cf6"/><path d="M11.5 12v7M8 15.5h7" stroke="#fff" stroke-width="2"/></svg></div>
    <h3>EMERGENCY CARE</h3>
    <p>Lorem ipsum dolor sit ametsicing elit sed do eiusmod temp.</p>
    <div class="go"><svg width="16" height="8" viewBox="0 0 16 8"><path d="M0 4h14M11 1l3 3-3 3" stroke="#333" stroke-width="1.3" fill="none"/></svg></div>
  </div>
  <div class="card" style="left:356px">
    <div class="hex"><svg viewBox="0 0 30 30"><path d="M9 4c-4 0-6 3-5 8 1 4 2 6 3 12 .5 3 3 3 3.5 0l1-5c.5-2 2.5-2 3 0l1 5c.5 3 3 3 3.5 0 1-6 2-8 3-12 1-5-1-8-5-8-2 0-3 1-4 1s-2-1-4-1z" fill="#19b37a"/></svg></div>
    <h3>DENTAL CARE</h3>
    <p>Lorem ipsum dolor sit ametsicing elit sed do eiusmod temp.</p>
    <div class="go"><svg width="16" height="8" viewBox="0 0 16 8"><path d="M0 4h14M11 1l3 3-3 3" stroke="#333" stroke-width="1.3" fill="none"/></svg></div>
  </div>
  <div class="card" style="left:614px">
    <div class="hex"><svg viewBox="0 0 30 30"><path d="M15 26S3 18 3 10.5A6 6 0 0 1 15 8a6 6 0 0 1 12 2.5C27 18 15 26 15 26z" fill="#e0457b"/><path d="M19 11v7M15.5 14.5h7" stroke="#fff" stroke-width="2"/></svg></div>
    <h3>HEART DISEASE</h3>
    <p>Lorem ipsum dolor sit ametsicing elit sed do eiusmod temp.</p>
    <div class="go"><svg width="16" height="8" viewBox="0 0 16 8"><path d="M0 4h14M11 1l3 3-3 3" stroke="#333" stroke-width="1.3" fill="none"/></svg></div>
  </div>
  <div class="card" style="left:870px">
    <div class="hex"><svg viewBox="0 0 30 30"><path d="M15 3S6 13 6 19a9 9 0 0 0 18 0C24 13 15 3 15 3z" fill="#f0643c"/><path d="M15 15v7M11.5 18.5h7" stroke="#fff" stroke-width="2"/></svg></div>
    <h3>BLOOD TEST</h3>
    <p>Lorem ipsum dolor sit ametsicing elit sed do eiusmod temp.</p>
    <div class="go"><svg width="16" height="8" viewBox="0 0 16 8"><path d="M0 4h14M11 1l3 3-3 3" stroke="#333" stroke-width="1.3" fill="none"/></svg></div>
  </div>
</section>

<section class="quiz abs">
  <div class="quiz-person abs" role="img" aria-label="Young male doctor in a white coat and blue tie with a stethoscope"></div>
  <h2 class="heading">QUIZ SECTION</h2>

  <div class="q" style="top:130px">1. I am</div>
  <ul class="opts" style="top:128px">
    <li><span class="radio"></span>Over 64 years old</li>
    <li><span class="radio"></span>64 years old</li>
    <li><span class="radio on"></span>Under 64 years old</li>
  </ul>

  <div class="q" style="top:257px">2. I am</div>
  <ul class="opts" style="top:255px">
    <li><span class="radio on"></span>Male</li>
    <li><span class="radio"></span>Female</li>
    <li><span class="radio"></span>Unspecified</li>
  </ul>

  <div class="q" style="top:383px">3. I want to see</div>
  <ul class="opts" style="top:381px">
    <li><span class="radio on"></span>Free plans</li>
    <li><span class="radio"></span>Premium plans</li>
    <li><span class="radio"></span>All plans</li>
  </ul>

  <div class="zip">[enter zip code]</div>
  <div class="submit">Submit</div>
</section>

<section class="explain abs">
  <h2 class="heading">What is a Medicare Supplement plan?</h2>
  <div class="photo abs" role="img" aria-label="Doctor caring for a smiling young girl in a hospital bed"></div>
  <div class="body">
    <p>Each Medicare Supplement insurance plan offers a different level of basic benefits, but each lettered plan will include the same standardized basic benefits regardless of insurance company and location.</p>
    <p>Medicare Supplement insurance plans do not always cover vision, dental, long-term care, or hearing aids, but all plans must cover at least a portion of the following basic benefits:</p>
    <ul>
      <li>Medicare Part A coinsurance costs up to an additional 365 days after Medicare benefits are exhausted</li>
      <li>Medicare Part A hospice care coinsurance or copayments</li>
      <li>Medicare Part B coinsurance or copayments</li>
      <li>First three pints of blood used in a medical procedure</li>
    </ul>
  </div>
</section>

<section class="costs abs">
  <h2 class="heading">Medicare Supplement Insurance Plan Costs</h2>
  <div class="rule"></div>
  <div class="body">
    <p>Although private insurance companies are required to offer the same basic benefits for each lettered plan, they do have the ability to charge different premiums. You might want to shop around to find a Medicare Supplement Insurance plan that may fit your medical and financial needs. Insurance companies may price their plan premiums in any of the following ways:</p>
    <p class="item">Community no-age-rated: These Medicare Supplement insurance plans charge premiums that are the same across the board, regardless of age.</p>
    <p class="item" style="margin-bottom:0">Issue-age-rated: These plans base their premiums on your age when you first enrolled in the policy. Therefore, the younger you are when you enroll in this type of plan, the lower your premium will be.</p>
    <p class="item">Attained-age-rated: Like issue-age-rated, these plans base their premiums on the age you were when you first bought a policy, but unlike issue-age-rated, premiums increase as you get older. Please note that no matter what rating method an insurance company uses, premiums may increase over time for reasons other than age, such as inflation.</p>
  </div>
  <div class="photo abs" role="img" aria-label="Team of doctors discussing notes around a table"></div>
</section>

<section class="newsletter abs">
  <h2>Don’t Miss Any<br>Update</h2>
  <div class="divider"></div>
  <div class="label">Get Update From Anywhere</div>
  <div class="signup">Enter Your Email Here
    <span class="send"><svg width="20" height="20" viewBox="0 0 20 20"><path d="M2 10l16-7-5 15-3-6z" fill="#fff"/></svg></span>
  </div>
</section>

<section class="map abs" role="img" aria-label="Street map showing the office location">
  <div class="zoom">+<br>−</div>
  <div class="full"></div>
</section>

<footer class="site-footer abs">
  <div class="foot-brand"><span class="mark"></span>BRIGHT HARBOR HEALTH</div>
  <p class="foot-about">Lorem ipsum dolor sit amet onsectetur adipi sicing elit, sed do eiusmod tempor incididunt ut labore et onsectetur adipisicing elit dolore a aliquia. Ut enim ad minim veniam quis nstrud exercitation ullamco.</p>

  <div class="foot-col" style="left:443px">
    <h4>Quick Links</h4>
    <ul style="padding-left:4px"><li>Home</li><li>About</li><li>Blog</li><li>Service</li><li>Portfolio</li></ul>
  </div>
  <div class="foot-col" style="left:614px">
    <h4>Social Media</h4>
    <ul><li><span class="dot"></span>Circlepost</li><li><span class="dot"></span>Plusline</li><li><span class="dot"></span>Chirper</li><li><span class="dot"></span>Workweb</li><li><span class="dot"></span>Chatwave</li></ul>
  </div>
  <div class="foot-col find" style="left:872px">
    <h4>Find Us</h4>
    <ul>
      <li><svg viewBox="0 0 14 14"><path d="M7 1L1 6.5h2V13h3V9h2v4h3V6.5h2z" fill="#fff"/></svg><span>27 Linden Quay<br>Harborfield HB4 2QT<br>United Kingdom</span></li>
      <li><svg viewBox="0 0 14 14"><rect x="1" y="3" width="12" height="9" rx="1" fill="none" stroke="#fff" stroke-width="1.4"/><path d="M1.5 3.5L7 8l5.5-4.5" fill="none" stroke="#fff" stroke-width="1.4"/></svg><span>hello@brightharborhealth.com</span></li>
      <li><svg viewBox="0 0 14 14"><path d="M3 1l2.5 3-1.5 1.5a8 8 0 0 0 4.5 4.5L10 8.5l3 2.5-1.5 2C6 13 1 8 1 2.5z" fill="#fff"/></svg><span>+1800 555 0192</span></li>
    </ul>
  </div>
</footer>
<div class="copyright abs">© Copyright reserved, Bright Harbor Health</div>

</body>
</html>
```